Truck Wrap Design for Pebble Lane Movers

We need a moving box truck wrapped with our catch phrase "We wrap, We strap, we'll spare your back. Call Pebble Lane!", our phone number "Call now (812) 640-3917, our FB page, instagram page, QR code, website: pebblelanemovers.example, professional yet eye catching with our logo (uploaded). Truck information document attached as well showing dimensions of the vehicle. We would like some designs with color rather than black and white options.
Updates

Hey guys. We're really liking the efforts but would like to see more color in the designs. Something professional and simple.

Low design entry and low design quality submissions.

Target Market(s)

Families and older people

Industry/Entity Type

Moving

Requirements
Must have
• Contact information and catch phrase
Nice to have
• Professional and eye catching

```html
<!DOCTYPE html>
<html lang="en">
<head>
<meta charset="utf-8">
<title>Pebble Lane Movers – Truck Wrap</title>
<link rel="stylesheet" href="https://fonts.googleapis.com/css2?family=Jost:wght@500&family=Oswald:wght@500&family=Poppins:wght@400;600&display=swap">
<style>
  :root {
    --ink: #0d0d0d;
    --accent: #1f3a5f;
    --paper: #ffffff;
    --stage: #e8e9eb;
    --edge: #cfd1d4;
    --art-light: #2a2a2a;
    --badge: #b3b6bb;
  }
  * { box-sizing: border-box; margin: 0; padding: 0; }
  html, body { width: 1200px; height: 1200px; overflow: hidden; }
  body {
    background: var(--stage);
    position: relative;
    font-family: "Poppins", sans-serif;
  }
  .wrap-panel {
    position: absolute;
    left: 50px;
    width: 1100px;
    height: 430px;
    background: var(--paper);
    border: 1px solid var(--edge);
    overflow: hidden;
  }
  .wrap-panel--first { top: 120px; }
  .wrap-panel--second { top: 650px; }

  .hand-truck-art {
    position: absolute;
    left: 14px; top: 14px; bottom: 14px;
    width: 420px;
    background: linear-gradient(160deg, var(--art-light), var(--ink) 60%);
    clip-path: polygon(0 0, 8% 0, 100% 74%, 100% 100%, 0 100%);
  }
  .social-dots {
    position: absolute;
    left: 50px; bottom: 40px;
    display: flex; gap: 12px;
  }
  .social-dots span {
    width: 26px; height: 26px;
    border-radius: 50%;
    background: var(--paper);
  }

  .brand-mark {
    position: absolute;
    left: 420px; top: 60px;
    width: 150px; height: 150px;
    border-radius: 50%;
    background: var(--accent);
  }
  .brand-name {
    position: absolute;
    left: 600px; top: 92px;
    width: 485px;
    text-align: center;
    font-family: "Jost", sans-serif;
    font-weight: 500;
    font-size: 54px;
    line-height: 58px;
    letter-spacing: 1px;
    color: var(--ink);
    text-transform: uppercase;
    white-space: nowrap;
  }

  .tagline-band {
    position: absolute;
    left: 380px; right: 14px; top: 318px;
    height: 44px;
    background: var(--accent);
    color: var(--paper);
    font-family: "Oswald", sans-serif;
    font-weight: 500;
    font-size: 19px;
    letter-spacing: 1px;
    text-transform: uppercase;
    white-space: nowrap;
    display: flex; align-items: center; justify-content: flex-end;
    padding-right: 20px;
    clip-path: polygon(40px 0, 100% 0, 100% 100%, 0 100%);
  }

  .contact-row {
    position: absolute;
    left: 440px; right: 14px; top: 370px;
    height: 44px;
    display: flex; align-items: center; justify-content: space-between;
    padding: 0 20px 0 20px;
    color: var(--ink);
    white-space: nowrap;
  }
  .contact-row--dark {
    left: 440px;
    background: var(--accent);
    color: var(--paper);
  }
  .phone {
    font-weight: 600;
    font-size: 26px;
    white-space: nowrap;
  }
  .website {
    font-size: 19px;
    display: flex; align-items: center; gap: 8px;
    white-space: nowrap;
  }
  .website b { font-weight: 600; }
  .badge {
    width: 26px; height: 16px;
    background: var(--badge);
  }
</style>
</head>
<body>

  <section class="wrap-panel wrap-panel--first">
    <div class="hand-truck-art" role="img" aria-label="Large black illustration of a hand truck carrying stacked moving boxes"></div>
    <div class="social-dots"><span></span><span></span></div>
    <div class="brand-mark"></div>
    <h1 class="brand-name">Pebble Lane<br>Movers</h1>
    <p class="tagline-band">We wrap, We strap, we'll spare your back. Call Pebble Lane!</p>
    <div class="contact-row">
      <span class="phone">(812) 640-3917</span>
      <span class="website">www.<b>pebblelanemovers</b>.example <span class="badge"></span></span>
    </div>
  </section>

  <section class="wrap-panel wrap-panel--second">
    <div class="hand-truck-art" role="img" aria-label="Large black illustration of a hand truck carrying stacked moving boxes"></div>
    <div class="social-dots"><span></span><span></span></div>
    <div class="brand-mark"></div>
    <h1 class="brand-name">Pebble Lane<br>Movers</h1>
    <p class="tagline-band">We wrap, We strap, we'll spare your back. Call Pebble Lane!</p>
    <div class="contact-row contact-row--dark">
      <span class="phone">(812) 640-3917</span>
      <span class="website">www.<b>pebblelanemovers</b>.example</span>
    </div>
  </section>

</body>
</html>
```